Postcard flyer for body postive dance classes

We need an eye catching double sided A6 postcard for body positive dance classes. The business name is twirlbrightday and already have a rough logo and some text that needs tidying up and putting together. The design needs to be simple and elegant. We are appealing to a diverse range of adult women with or without dance experience to join us in a safe, supportive and creative environment. We would like the design to use black, white and a soft green. The final design should communicate movement, contentment and wholeness. File with information attached.

Target Market(s)

Diverse range of adult women

Industry/Entity Type

Health And Wellness

Font styles to use
Other font styles liked:
• Candara or similar but open to suggestions

Colors
abd036
cadf82
eaf2ce
fffefb
fef9ed
fff3d1
ffffff

Requirements
Must have
• Logo and text provided.
Nice to have
• Sense of movement. Match to website colours and style.
Should not have
• Intimidating perfect body images

```html
<!DOCTYPE html>
<html lang="en">
<head>
<meta charset="utf-8">
<title>twirlbrightday postcard</title>
<link href="https://fonts.googleapis.com/css2?family=Cabin:wght@400;500;600;700&display=swap" rel="stylesheet">
<style>
  :root {
    --green: #abd036;
    --green-soft: #cadf82;
    --cream: #fff3d1;
    --ink: #3b3b3b;
    --grey: #5f5f5f;
    --text: #2a2a2a;
    --row: #d9d9d9;
    --stamp: #ababab;
    --white: #ffffff;
  }
  * { margin: 0; padding: 0; box-sizing: border-box; }
  html, body { width: 1029px; height: 1200px; overflow: hidden; background: var(--white); }
  body { font-family: "Cabin", "Candara", sans-serif; color: var(--text); }
  .stage { position: absolute; left: 0; top: 0; width: 1200px; height: 1400px; transform: scale(0.8575); transform-origin: 0 0; }
  .card { position: absolute; width: 828px; height: 589px; background: var(--white); overflow: hidden; box-shadow: 2px 4px 10px rgba(0,0,0,.35); }
  .card--front { left: 188px; top: 73px; }
  .card--back { left: 185px; top: 748px; }
  .card svg.shapes { position: absolute; left: 0; top: 0; }
  .brand { position: absolute; display: flex; align-items: center; gap: 14px; }
  .brand__dot { width: 52px; height: 52px; border-radius: 50%; background: var(--green-soft); }
  .brand__name { font-size: 30px; font-weight: 400; color: var(--grey); letter-spacing: .5px; line-height: 1; }
  .headline { position: absolute; left: 30px; top: 170px; font-size: 44px; font-weight: 700; color: var(--green); line-height: 1; }
  .subhead { position: absolute; left: 31px; top: 223px; font-size: 29px; font-weight: 400; color: var(--grey); line-height: 1; }
  .body-copy { position: absolute; left: 30px; font-size: 15px; line-height: 19px; color: var(--text); }
  .body-copy span { display: block; white-space: nowrap; }
  .body-copy--justified span { text-align: justify; text-align-last: justify; white-space: normal; }
  .body-copy--justified span:last-child { text-align-last: left; }
  .web-strip { position: absolute; left: 0; bottom: 0; width: 100%; height: 52px; background: var(--ink); color: var(--white); font-size: 16px; letter-spacing: 8px; text-align: center; line-height: 52px; padding-left: 10px; }
  .pricing-title { position: absolute; left: 58px; top: 147px; width: 232px; display: flex; align-items: center; gap: 6px; color: var(--green); font-weight: 600; font-size: 19px; }
  .pricing-title i { flex: 1; height: 8px; background: #b5b5b5; }
  .pricing-title i:first-child { clip-path: polygon(0 50%, 100% 0, 100% 100%); }
  .pricing-title i:last-child { clip-path: polygon(0 0, 100% 50%, 0 100%); }
  .price-row { position: absolute; left: 32px; width: 290px; display: flex; justify-content: space-between; font-size: 16.5px; }
  .price-row b { font-weight: 700; }
  .start-date { position: absolute; left: 25px; top: 391px; font-size: 28px; font-weight: 600; color: var(--green); }
  .contact { position: absolute; color: #cfcfcf; font-size: 14px; }
  .contact--area { left: 24px; top: 486px; }
  .contact--area strong { display: block; color: var(--green); font-size: 18px; font-weight: 700; margin-top: 14px; }
  .contact--lines { left: 206px; top: 486px; line-height: 23px; }
  .contact--lines span { display: inline-block; width: 8px; height: 8px; border-radius: 50%; background: var(--green); margin-right: 4px; }
  .stamp { position: absolute; left: 723px; top: 25px; width: 72px; height: 89px; background: var(--stamp); }
</style>
</head>
<body>
<div class="stage">

  <section class="card card--front">
    <svg class="shapes" width="828" height="589" viewBox="0 0 828 589">
      <defs>
        <radialGradient id="photoTone" cx="0.6" cy="0.45" r="0.7">
          <stop offset="0" stop-color="#e6e6e6"/>
          <stop offset="1" stop-color="#8c8c8c"/>
        </radialGradient>
      </defs>
      <polygon points="487,0 828,0 828,537 375,537" fill="url(#photoTone)" role="img" aria-label="Photo of a dancer leaping mid-air against a grey studio backdrop"/>
      <polygon points="476,0 482,0 370,537 364,537" fill="var(--cream)"/>
      <polygon points="481,0 487,0 375,537 369,537" fill="var(--green)"/>
    </svg>
    <div class="brand" style="left:32px; top:60px;">
      <div class="brand__dot"></div>
      <div class="brand__name">twirlbrightday</div>
    </div>
    <h1 class="headline">WE BELIEVE THAT</h1>
    <h2 class="subhead">DANCE IS FOR EVERYONE</h2>
    <p class="body-copy" style="top:307px;">
      <span>Dance is joy, dance is love. Dance is at the core of our</span>
      <span>being, a celebration of movement, vitality</span>
      <span>and wholeness.</span>
    </p>
    <p class="body-copy body-copy--justified" style="top:382px; left:33px; width:318px;">
      <span>If you’ve never danced before and always</span>
      <span>wanted to or you want to reignite your past love</span>
      <span>of dance, join us at twirlbrightday to start your</span>
      <span>journey.</span>
    </p>
    <div class="web-strip">www.twirlbrightday.com.au</div>
  </section>

  <section class="card card--back">
    <svg class="shapes" width="828" height="589" viewBox="0 0 828 589">
      <polygon points="0,197 358,197 365,230 0,230" fill="var(--row)"/>
      <polygon points="0,233 366,233 372,266 0,266" fill="var(--row)"/>
      <polygon points="0,268 373,268 380,302 0,302" fill="var(--row)"/>
      <polygon points="0,304 380,304 387,342 0,342" fill="var(--row)"/>
      <polygon points="0,452 412,452 437,589 0,589" fill="var(--ink)"/>
      <polygon points="331,0 337,0 454,589 448,589" fill="var(--cream)"/>
      <polygon points="324,0 331,0 447,589 440,589" fill="var(--green)"/>
    </svg>
    <div class="brand" style="left:28px; top:54px;">
      <div class="brand__dot" style="width:48px;height:48px;"></div>
      <div class="brand__name" style="font-size:27px;">twirlbrightday</div>
    </div>
    <div class="pricing-title"><i></i>Pricing<i></i></div>
    <div class="price-row" style="top:207px;">Introductory class<b>$15</b></div>
    <div class="price-row" style="top:242px;">Casual<b>$22</b></div>
    <div class="price-row" style="top:276px;">Pack of 6 weeks<b>$120</b></div>
    <div class="price-row" style="top:311px;">Private lesson<b>$80</b></div>
    <div class="start-date">Classes start January 2017</div>
    <div class="contact contact--area">Contact<strong>Birchwood/Larkfield</strong></div>
    <div class="contact contact--lines">
      <span></span>0400518276<br>
      <span></span>maya@twirlbrightday.com.au<br>
      <span></span>www.twirlbrightday.com.au
    </div>
    <div class="stamp"></div>
  </section>

</div>
</body>
</html>
```